Wordpress Design for Software Company

I have a website that is not developed in WordPress. I need the current site www.brenwix.com/projects/tormelink to be redesigned in Wordpress. I would to keep some of the look and feel but change other things.
1) such as logo background color
2) have (3) columns in on inner pages
3) so nice pictures or graphic layouts I am hoping that you will be able to improve on the look of the website.
Target Market(s)
B2B Companies that deploy call centers or have inside sales staff.
Industry/Entity Type
It Company
Look and feel

```html
<!DOCTYPE html>
<html lang="en">
<head>
<meta charset="utf-8">
<title>TormeLink – Enterprise Solutions</title>
<link href="https://fonts.googleapis.com/css2?family=Ubuntu:wght@300;400;500&family=Arimo:wght@400&display=swap" rel="stylesheet">
<style>
:root{
  --header-dark:#0c3147;
  --header-mid:#1d5f82;
  --nav-dark:#0e2735;
  --btn-dark:#1a3444;
  --brand-blue:#2aa3d9;
  --sky:#3ab0e3;
  --light-blue:#8fd8ff;
  --orange:#f7931e;
  --text:#5a5a5a;
  --ink:#222;
  --peach-top:#fdbf84;
  --peach-bot:#fee7cf;
  --copy:#d4361b;
}
*{box-sizing:border-box;margin:0;padding:0}
html,body{width:1200px;height:1023px;overflow:hidden}
body{
  font-family:"Ubuntu",sans-serif;
  background:
    radial-gradient(ellipse 220px 700px at 0 420px,#9fcbef 0%,rgba(255,255,255,0) 100%),
    radial-gradient(ellipse 220px 700px at 1280px 420px,#9fcbef 0%,rgba(255,255,255,0) 100%),
    #fff;
}
.stage{position:absolute;left:0;top:0;width:1280px;height:1067px;transform-origin:0 0;transform:scale(0.9375,0.9588)}
.abs{position:absolute}
.page{position:absolute;left:139px;top:0;width:1002px;height:1013px;box-shadow:0 0 12px rgba(40,90,140,.25)}

/* header */
.site-header{left:0;top:0;width:1002px;height:95px;background:linear-gradient(180deg,var(--header-dark),var(--header-mid) 60%,#184e6c)}
.brand{left:22px;top:18px;display:flex;align-items:center;gap:10px}
.brand-dot{width:44px;height:44px;border-radius:50%;background:var(--orange)}
.brand-name{font-size:30px;color:var(--orange);font-weight:400}
.login{right:26px;top:11px;font-size:14px;color:var(--light-blue)}
.search{right:22px;top:47px;width:279px;height:35px;background:var(--brand-blue);border-radius:2px}
.search-field{left:14px;top:8px;width:213px;height:20px;background:#1d7fae}
.search-icon{right:12px;top:5px}

/* nav */
.main-nav{left:0;top:95px;width:1002px;height:46px;background:var(--nav-dark);border-top:1px solid #4a7a94}
.nav-btn{top:6px;width:154px;height:34px;border-radius:3px;background:linear-gradient(#243e4f,#12283a);border:1px solid #000;color:var(--sky);font-size:16px;display:flex;align-items:center;justify-content:center}
.nav-btn.is-active{background:linear-gradient(#3bb4ea,#1a7fb6);color:#0b1d29}
.social{top:7px;width:30px;height:30px;border-radius:50%;background:#2f7fc0}

/* breadcrumb */
.breadcrumb{left:0;top:141px;width:1002px;height:36px;background:linear-gradient(#38aee2,#2598cf);font-size:14px;color:#0b2030}
.crumb{top:9px}

/* columns */
.col-side{top:178px;width:218px;height:611px;background:linear-gradient(180deg,#fff 8%,#cfeefc 30%,var(--brand-blue) 100%)}
.col-head{left:0;top:0;width:218px;height:38px;background:linear-gradient(#2b3c47,#0e1c25);color:#fff;font-size:17px;display:flex;align-items:center;gap:10px;padding-left:10px}
.col-head .dot{width:14px;height:14px;border-radius:50%;background:var(--orange)}
.side-list{list-style:none;position:absolute;left:15px;top:52px;font-size:12.5px;color:#27323a}
.side-list li{height:24px;display:flex;gap:8px}
.side-list li::before{content:"›";font-weight:500;font-size:15px;line-height:14px}
.info-box{left:18px;width:177px;background:#fff;border-radius:4px;box-shadow:0 1px 3px rgba(0,0,0,.2);font-family:"Arimo",sans-serif;font-size:12px;color:#111}
.learn{position:absolute;right:9px;font-size:10px;color:var(--orange);text-decoration:underline}

.col-main{left:219px;top:178px;width:564px;height:623px;background:#fff;padding:12px 12px 0 13px}
.col-main h2{font-size:21px;font-weight:400;color:var(--orange);margin-bottom:4px}
.col-main p{font-size:12.3px;font-weight:300;color:var(--text);line-height:22px;letter-spacing:-.1px}
.col-main p+p{margin-top:22px}

/* footer */
.site-footer{left:0;top:801px;width:1002px;height:212px;background:linear-gradient(var(--peach-top),var(--peach-bot))}
.foot-col{top:15px;font-size:12px;color:var(--ink);line-height:18px}
.foot-col h3{font-size:16px;font-weight:400;margin-bottom:6px;display:flex;align-items:center;gap:5px}
.foot-col h3::before{content:"";width:5px;height:5px;background:#e8611e}
.foot-rule{top:25px;width:1px;height:165px;background:rgba(200,140,80,.3)}
.copyright{left:0;top:1038px;width:1280px;text-align:center;font-family:"Arimo",sans-serif;font-size:11px;color:var(--copy)}
</style>
</head>
<body>
<div class="stage">
  <div class="page">
    <header class="site-header abs">
      <div class="brand abs"><span class="brand-dot"></span><span class="brand-name">TormeLink</span></div>
      <span class="login abs">Login</span>
      <div class="search abs">
        <div class="search-field abs"></div>
        <svg class="search-icon abs" width="26" height="26" viewBox="0 0 26 26"><circle cx="10" cy="10" r="7" fill="none" stroke="#fff" stroke-width="2.5"/><line x1="15" y1="15" x2="23" y2="23" stroke="#fff" stroke-width="4" stroke-linecap="round"/></svg>
      </div>
    </header>

    <nav class="main-nav abs">
      <div class="nav-btn abs" style="left:10px">Products</div>
      <div class="nav-btn abs is-active" style="left:171px">Solutions</div>
      <div class="nav-btn abs" style="left:331px">Resources</div>
      <div class="nav-btn abs" style="left:493px">Services</div>
      <span class="social abs" style="left:876px"></span>
      <span class="social abs" style="left:918px"></span>
      <span class="social abs" style="left:958px;background:#e8611e"></span>
    </nav>

    <div class="breadcrumb abs">
      <svg class="abs" style="left:12px;top:10px" width="16" height="16" viewBox="0 0 16 16"><path d="M8 1 1 8h2v7h4v-4h2v4h4V8h2z" fill="#0b2030"/></svg>
      <svg class="abs" style="left:34px;top:0" width="20" height="36" viewBox="0 0 20 36"><path d="M2 0 16 18 2 36" fill="none" stroke="#7ccdf0" stroke-width="2"/></svg>
      <span class="crumb abs" style="left:63px">Solutions</span>
      <svg class="abs" style="left:134px;top:0" width="20" height="36" viewBox="0 0 20 36"><path d="M2 0 16 18 2 36" fill="none" stroke="#7ccdf0" stroke-width="2"/></svg>
      <span class="crumb abs" style="left:169px">Enterprise</span>
      <svg class="abs" style="left:234px;top:0" width="20" height="36" viewBox="0 0 20 36"><path d="M2 0 16 18 2 36" fill="none" stroke="#7ccdf0" stroke-width="2"/></svg>
    </div>

    <aside class="col-side abs" style="left:1px">
      <div class="col-head abs"><span class="dot"></span>Solutions</div>
      <ul class="side-list">
        <li>Hosted Solutions</li><li>Premise Based</li><li>Industry Specific</li>
        <li>Small Office</li><li>Mid Size</li><li>Enterprise</li>
      </ul>
      <div class="info-box abs" style="top:391px;height:58px">
        <svg class="abs" style="left:12px;top:9px" width="14" height="20" viewBox="0 0 14 20"><path d="M8 0 1 11h5l-2 9 9-12H8l2-8z" fill="#f5b21e"/></svg>
        <div class="abs" style="left:33px;top:8px;line-height:14px">Predictive Dialing 101<br>white papers</div>
        <span class="learn" style="top:37px">▸ Learn more</span>
      </div>
      <div class="info-box abs" style="top:465px;height:58px">
        <svg class="abs" style="left:11px;top:15px" width="16" height="18" viewBox="0 0 16 18"><rect x="1" y="1" width="13" height="16" fill="#fff" stroke="#c33"/><rect x="3" y="8" width="9" height="6" fill="#d22"/></svg>
        <div class="abs" style="left:34px;top:16px">Request Brochure</div>
        <span class="learn" style="top:38px">▸ Learn more</span>
      </div>
      <div class="info-box abs" style="top:537px;height:57px">
        <svg class="abs" style="left:8px;top:12px" width="14" height="12" viewBox="0 0 14 12"><path d="M1 4c3-4 9-4 12 0l-2 2-2-1V3H5v2L3 6z M3 7h8v5H3z" fill="#e8611e"/></svg>
        <div class="abs" style="left:29px;top:10px;font-size:14px">1.888.555.0142 <span style="font-size:9px;color:#e8611e">(Toll-free)</span></div>
        <svg class="abs" style="left:8px;top:35px" width="14" height="10" viewBox="0 0 14 10"><rect width="14" height="10" fill="#f5a43a"/><path d="M0 0 7 6 14 0" fill="none" stroke="#fff"/></svg>
        <div class="abs" style="left:29px;top:33px;font-size:11px">mira@tormelinkcorp.com</div>
      </div>
    </aside>

    <main class="col-main abs">
      <h2>Cloud Based Call Center</h2>
      <p>Torme Link Corps Hosted Predictive Dialer Contact Center Solution gives you the leverage you need to start your call center with as little capital expenditure right from the get go . Imagine having he ability to test market a new campaign using a hosted Contact Center Solution where you can select from a list of different industry specific applications to choose from.</p>
      <p>With the advent of the new economy and the Internet a variety of hosted solutions are available where you do not have to invest in any hardware or incur any long distance charges. Simply log on to our Hosted Telephony Servers and select from a variety of existing applications already created for your call center. So whether you are in the mortgage business, collections business, resorts, insurance, debt consolidation business or just doing B2B we have the</p>
      <h2 style="margin-top:12px">Remote In Home Agent</h2>
      <p>Gives you the leverage you need, now your contact center is not limited to geographic boundaries. Agents can log in from anywhere using a browser to utilize the CallStation Hosted Predictive Dialer to take incoming and outgoing calls. Reports will be easy accessible so that even if your reps aren't in your office you can still keep track of their work and performance.solutions already built for you.</p>
      <h2 style="margin-top:6px">Hosted Auto Dialing Solution Suite</h2>
      <p>Hosted On demand Dialing gives you the flexibility to immediately start making calls. This on demand dialing feature is simple and easy to use. User simply logs in to their account and select records to be dialed for a particular campaign. Voice broadcasting.</p>
      <h2 style="margin-top:12px">Customized IVR (Interactive Voice Response) Scripts</h2>
      <p>Part of the suite of CTI Solutions is IVR which gives your customers the ability can get instant information on products and services over the phone with Database integration.</p>
    </main>

    <aside class="col-side abs" style="left:783px">
      <div class="col-head abs"><span class="dot"></span>Right col</div>
      <ul class="side-list" style="top:53px">
        <li>Lorem Ipsum is simply</li><li>dummy text of the printing</li><li>and typesetting industry.</li>
        <li>Lorem Ipsum has been the</li><li>industry's standard dummy</li><li>text ever since the 1500s,</li>
        <li>when an unknown printer</li><li>took a galley of type and</li><li>scrambled it</li>
      </ul>
    </aside>

    <footer class="site-footer abs">
      <div class="foot-col abs" style="left:24px">
        <h3>Products</h3>
        CallStation™ Premise Based Predictive Dialer<br>Inbound/Outbound blended Dialer &amp; ACD<br>Hosted Predictive Dialer/IP<br>Contact Center<br>Contact Manager CRM<br>Auto, Preview and progressive&nbsp; Dialing<br>IVR/CallVoice<br>Digital Call Recording
      </div>
      <span class="foot-rule abs" style="left:284px"></span>
      <div class="foot-col abs" style="left:317px">
        <h3>Solutions</h3>
        Industry Specific<br>Premise Based<br>Hosted Solutions<br>Small Office<br>Mid Size<br>Enterprise<br>Business Integration<br>Computer Telephony (CTI)
      </div>
      <span class="foot-rule abs" style="left:503px"></span>
      <div class="foot-col abs" style="left:534px">
        <h3>Features</h3>
        Our sales and metro areas,<br>support teams metro areas,metro areas,<br>are located in metro areas,<br>more than 30<br>metro areas,metro areas,<br>&nbsp;including<br>Atlanta,
      </div>
      <span class="foot-rule abs" style="left:761px"></span>
      <div class="foot-col abs" style="left:787px">
        <h3>Resources</h3>
        Press Room
      </div>
    </footer>
  </div>
  <p class="copyright abs">© 2011 tormelinkcorp. All Rights Reserved.</p>
</div>
</body>
</html>
```